We need letterhead, Business Cards, and envelops designed. We have attached a design of our logo and a sample of letterhead idea that was started but never perfected, it is only an idea for the letterhead if you can design something better we may love that also we are open to change.
We want a design that looks professional in style. we are a non profit trade association in the construction industry. the green color in the attached design represent green building, and we like that. also if you just want to enhance the letterhead sample that we attached that would be fine also.
Thanks and good luck
also the name that should show on the first business cards should be Merwin Habsfield, Director are web address is www.tqvmp.org

```html
<!DOCTYPE html>
<html lang="en">
<head>
<meta charset="utf-8">
<title>TQVMP Business Card</title>
<link rel="stylesheet" href="https://fonts.googleapis.com/css2?family=Cabin:wght@400&family=Arimo:wght@400&display=swap">
<style>
  :root {
    --page: #ffffff;
    --ink: #111111;
    --lime: #8efc2a;
    --pale-green: #c5e2bd;
    --card-edge: #1a1a1a;
  }
  html, body {
    margin: 0;
    padding: 0;
    width: 1200px;
    height: 960px;
    overflow: hidden;
    background: var(--page);
  }
  .canvas {
    position: relative;
    width: 1200px;
    height: 960px;
  }
  .card {
    position: absolute;
    left: 156px;
    top: 218px;
    width: 878px;
    height: 515px;
    background: var(--page);
    border: 1.5px solid var(--card-edge);
    box-sizing: border-box;
    overflow: hidden;
    font-family: "Cabin", sans-serif;
    color: var(--ink);
  }
  .contact-panel {
    position: absolute;
    left: 0;
    top: 0;
    width: 335px;
    height: 100%;
    background: var(--lime);
  }
  .top-band {
    position: absolute;
    left: 335px;
    top: 0;
    width: 236px;
    height: 28px;
    background: var(--lime);
  }
  .contact-list {
    position: absolute;
    left: 50px;
    top: 264px;
    margin: 0;
    padding: 0;
    list-style: none;
    font-size: 21px;
    line-height: 44px;
  }
  .contact-list .web {
    font-family: "Arimo", sans-serif;
    font-size: 20px;
  }
  .brand {
    position: absolute;
    left: 372px;
    top: 48px;
    width: 450px;
    text-align: center;
  }
  .brand-name {
    display: block;
    font-size: 118px;
    line-height: 1;
    letter-spacing: 6px;
    color: var(--ink);
  }
  .brand-full {
    display: block;
    margin-top: 8px;
    font-size: 18px;
    letter-spacing: 0.5px;
    color: var(--ink);
  }
  .person {
    position: absolute;
    left: 584px;
    top: 262px;
  }
  .person-name {
    margin: 0;
    font-size: 31px;
    font-weight: 400;
    line-height: 1.1;
  }
  .person-role {
    margin: 2px 0 0;
    font-size: 22px;
    line-height: 1.2;
  }
  .corner-square {
    position: absolute;
    left: 637px;
    top: 350px;
    width: 182px;
    height: 182px;
    background: var(--pale-green);
  }
</style>
</head>
<body>
<div class="canvas">
  <section class="card">
    <div class="contact-panel"></div>
    <div class="top-band"></div>

    <ul class="contact-list">
      <li>1420 Larkmoor Lane</li>
      <li>Fenwick Springs, CO 80940</li>
      <li>Tel: (719) 555-0148</li>
      <li>Email: info@tqvmp.org</li>
      <li class="web">www.tqvmp.org</li>
    </ul>

    <div class="brand">
      <span class="brand-name">TQVMP</span>
      <span class="brand-full">Tri-Quarter Valley Master Partners</span>
    </div>

    <div class="person">
      <h1 class="person-name">Merwin Habsfield</h1>
      <p class="person-role">Director</p>
    </div>

    <div class="corner-square" aria-hidden="true"></div>
  </section>
</div>
</body>
</html>
```